Information Technology Company needs a Website...

We need a single page website for new technology company called:

MERIDEL FALLS TECHNOLOGY GROUP
Based in Ojai CA.

We are offering three primary services:

- Business Solutions

- IT Services

- Software Implementation and Consulting

We want a single page design where all content scrolls down/up on one page. We're looking for the following characteristics:

- Home/Landing
- Active background with panoramic view (Will provide content)

- Business Solutions, IT Services, Software Implementation and Consulting

List of software vendors we recommend (Company logos)

- About
- History
- Our Team
- Partners

I'll upload our new logo as soon as we get the design files. I'll also send over some example website layout's that we like shortly.

Target Market(s)

Small/Medium Businesses

Industry/Entity Type

Information Technology

Number of Pages Required

1 page

Font styles to use
Other font styles liked:
• Sansation

Requirements
Must have
• Full page browser width, easy navigation and visibility. Creative design, not like every other "Technology" website template. Should be the "One Page" design where each section is below the next and the user scrolls down the page through the whole site. I like the concept of the following website in the main "Whiteboard" image:
• http://www.plavorix.com/design/4829137
• And the way this site does the active panoramic background:
• http://www.kelbrantworks.com/
• Something interesting and appealing to potential clients looking for Small/Medium business solutions and IT Services.
• Use uploaded Logo to establish color and theme for website.
Should not have
• Look the same as every other information technology website template.

```html
<!DOCTYPE html>
<html lang="en">
<head>
<meta charset="utf-8">
<title>Meridel Falls Technology Group</title>
<link href="https://fonts.googleapis.com/css2?family=Exo+2:wght@300;400;600;700&family=Open+Sans:wght@400;600&display=swap" rel="stylesheet">
<style>
:root{
  --orange:#f04e23;
  --dark:#3d3d3d;
  --footer:#4a4a4a;
  --grey-bg:#f3f3f3;
  --tab:#dcdcdc;
  --text:#555;
  --muted:#8a8a8a;
  --white:#fff;
}
*{box-sizing:border-box;margin:0;padding:0}
html,body{width:1200px;height:4852px;overflow:hidden}
body{position:relative;font-family:"Open Sans",Arial,sans-serif;color:var(--text);background:var(--white)}
h2.section-title{position:absolute;left:0;width:1200px;text-align:center;font-family:"Exo 2",Arial,sans-serif;font-weight:300;font-size:44px;color:#333;letter-spacing:1px}
h2.section-title span{color:var(--orange)}
.sub-title{position:absolute;left:0;width:1200px;text-align:center;font-family:"Exo 2",Arial,sans-serif;font-weight:600;font-size:30px;color:var(--orange);letter-spacing:1px}
.sub-note{position:absolute;left:0;width:1200px;text-align:center;font-size:17px;color:#666}

/* hero */
.hero{position:absolute;left:0;top:0;width:1200px;height:705px}
.hero-art{position:absolute;inset:0;background:linear-gradient(180deg,#4f4f4f 0%,#3b3b3b 60%,#474747 100%)}
.hero-city{position:absolute;left:0;bottom:0;width:1200px;height:110px;background:linear-gradient(180deg,rgba(255,255,255,0) 0%,rgba(255,255,255,.18) 100%)}
.topbar{position:absolute;left:0;top:0;width:1200px;height:125px;background:rgba(40,40,40,.55)}
.brand{position:absolute;left:80px;top:26px;font-family:"Exo 2",Arial,sans-serif;font-weight:600;font-size:26px;line-height:32px;color:var(--white);letter-spacing:1px;width:330px}
.nav{position:absolute;left:462px;top:68px;display:flex;gap:32px;list-style:none}
.nav li{font-family:"Exo 2",Arial,sans-serif;font-size:18px;color:var(--white);letter-spacing:.5px}
.social-top{position:absolute;left:958px;top:14px;display:flex;gap:10px}
.social-top span{width:32px;height:32px;border-radius:50%;background:var(--orange);display:block}
.hero-title{position:absolute;left:50px;top:205px;font-family:"Exo 2",Arial,sans-serif;font-weight:700;font-size:46px;line-height:54px;color:var(--white);letter-spacing:1px}
.hero-text{position:absolute;left:50px;top:322px;font-size:20px;line-height:30px;color:var(--white)}

/* welcome */
.welcome{position:absolute;left:0;top:705px;width:1200px;height:220px;background:var(--white)}
.welcome h1{position:absolute;left:0;top:50px;width:1200px;text-align:center;font-family:"Exo 2",Arial,sans-serif;font-weight:300;font-size:44px;color:#333;letter-spacing:1px}
.welcome h1 span{color:var(--orange)}
.welcome p{position:absolute;left:300px;top:118px;width:600px;text-align:center;font-size:14px;line-height:22px;color:var(--muted)}

/* services */
.services{position:absolute;left:0;top:925px;width:1200px;height:2000px;background:var(--grey-bg)}
.biz-item{position:absolute;width:200px;text-align:center;font-size:18px;line-height:26px;color:#555}
.biz-item svg{display:block;margin:0 auto 10px}
.divider{position:absolute;left:330px;width:540px;height:30px;border-radius:50%;box-shadow:0 18px 18px -14px rgba(0,0,0,.25)}
.tab{position:absolute;width:172px;height:170px;background:var(--tab);text-align:center;padding-top:28px;font-size:16px;line-height:22px;color:#444}
.tab svg{display:block;margin:0 auto 12px}
.tab.active{background:var(--orange);color:var(--white)}
.tab-detail h3{position:absolute;left:78px;top:1020px;font-family:"Exo 2",Arial,sans-serif;font-weight:300;font-size:40px;line-height:50px;color:#333}
.tab-detail h3 b{font-weight:600}
.btn-orange{position:absolute;background:var(--orange);color:var(--white);font-size:18px;padding:10px 18px;letter-spacing:.5px}
.tab-detail p{position:absolute;left:512px;width:610px;font-size:14px;line-height:22px;color:#555}
.card{position:absolute;top:1655px;width:190px;height:242px;background:var(--white);border:2px solid #e2e2e2;text-align:center;padding-top:28px;font-size:17px;line-height:24px;color:#555}
.card svg{display:block;margin:0 auto 10px}
.card .more{position:absolute;left:0;bottom:24px;width:100%;color:var(--orange);font-size:16px}

/* about */
.about{position:absolute;left:0;top:2925px;width:1200px;height:625px;background:var(--white)}
.about p{position:absolute;left:140px;top:165px;width:920px;text-align:center;font-size:14px;line-height:24px;color:#555}
.value{position:absolute;top:340px;width:200px;text-align:center;font-size:23px;line-height:32px;color:#444}
.value .dot{width:112px;height:112px;border-radius:50%;background:var(--orange);margin:0 auto 16px;display:flex;align-items:center;justify-content:center}

/* team */
.team{position:absolute;left:0;top:3550px;width:1200px;height:420px;background:var(--grey-bg)}
.member{position:absolute;top:135px;width:240px;text-align:center;font-size:20px;color:var(--orange)}
.avatar{width:146px;height:146px;border-radius:50%;background:radial-gradient(circle at 50% 45%,#ffffff 0%,#e4e4e4 70%,#cfcfcf 100%);border:4px solid #fff;box-shadow:0 0 0 1px #ddd;margin:0 auto 34px}

/* partners */
.partners{position:absolute;left:0;top:3970px;width:1200px;height:335px;background:var(--white)}
.partner-row{position:absolute;display:flex;align-items:center;justify-content:space-between}
.partner{font-family:"Exo 2",Arial,sans-serif;font-weight:600;font-size:28px;color:#666;white-space:nowrap;text-align:center}
.partner.small{font-size:22px;line-height:24px}

/* footer */
.footer{position:absolute;left:0;top:4305px;width:1200px;height:547px;background:var(--footer);color:var(--white)}
.footer h4{position:absolute;font-family:"Exo 2",Arial,sans-serif;font-weight:400;font-size:38px;letter-spacing:1px}
.rule{position:absolute;height:2px;background:var(--white)}
.rule::after{content:"";position:absolute;right:-6px;top:-5px;width:12px;height:12px;border-radius:50%;background:var(--white)}
.field{position:absolute;border:1.5px solid #ddd;font-size:13px;color:#eee;padding:8px 10px;height:40px}
.submit{position:absolute;left:78px;top:392px;width:165px;height:50px;border-radius:25px;background:var(--white);color:#333;font-size:17px;font-weight:600;display:flex;align-items:center;justify-content:center;letter-spacing:.5px}
.info{position:absolute;left:732px;font-size:15px;line-height:24px;display:flex;gap:14px}
.follow{position:absolute;left:728px;top:322px;font-size:22px;font-family:"Exo 2",Arial,sans-serif}
.social-foot{position:absolute;left:728px;top:362px;display:flex;gap:14px}
.social-foot span{width:50px;height:50px;border-radius:50%;border:2px solid var(--white);display:block}
.bottom-line{position:absolute;left:78px;top:497px;width:1044px;height:1px;background:#777}
.foot-links{position:absolute;left:78px;top:514px;display:flex;gap:18px;list-style:none;font-size:13px}
.foot-links li:first-child{color:var(--orange)}
.copy{position:absolute;right:78px;top:514px;font-size:13px}
.copy b{font-weight:600}
</style>
</head>
<body>

<header class="hero">
  <div class="hero-art" role="img" aria-label="Chalkboard illustration with hand-drawn technology words, business diagrams and a city skyline"></div>
  <div class="hero-city"></div>
  <div class="topbar"></div>
  <div class="brand">MERIDEL FALLS<br>TECHNOLOGY GROUP</div>
  <ul class="nav"><li>SERVICES</li><li>ABOUT US</li><li>OUR TEAM</li><li>PARTNERS</li><li>CONTACT US</li></ul>
  <div class="social-top" aria-label="Social links"><span></span><span></span><span></span><span></span></div>
  <h1 class="hero-title">YOUR TECHNOLOGY<br>BUSINESS PARTNER.</h1>
  <p class="hero-text">IT Services You Can Trust.<br>Technology Solutions To Help Grow Your Business.</p>
</header>

<section class="welcome">
  <h1>WELCOME TO <span>MERIDEL FALLS TECHNOLOGY GROUP</span></h1>
  <p>We've got you covered. From software consulting, implementation and support, to managed IT and cloud services.<br>Remove IT headaches and just focus on growing your business.</p>
</section>

<section class="services">
  <h2 class="section-title" style="top:55px">OUR <span>SERVICES</span></h2>
  <div class="sub-title" style="top:138px">BUSINESS SOLUTIONS</div>
  <div class="sub-note" style="top:184px">For small and medium businesses</div>

  <div class="biz-item" style="left:72px;top:255px"><svg width="60" height="50" viewBox="0 0 60 50"><path d="M15 40h32a10 10 0 0 0 0-20 14 14 0 0 0-27-3 11 11 0 0 0-5 23z" fill="var(--orange)"/></svg>Cloud Computing</div>
  <div class="biz-item" style="left:278px;top:255px"><svg width="60" height="50" viewBox="0 0 60 50"><rect x="22" y="2" width="16" height="12" fill="var(--orange)"/><rect x="4" y="34" width="16" height="12" fill="var(--orange)"/><rect x="40" y="34" width="16" height="12" fill="var(--orange)"/><path d="M30 14v10M12 34v-10h36v10" stroke="var(--orange)" stroke-width="3" fill="none"/></svg>Virtualization &amp;<br>Consolidation</div>
  <div class="biz-item" style="left:492px;top:255px"><svg width="60" height="50" viewBox="0 0 60 50"><rect x="10" y="14" width="40" height="30" rx="3" fill="var(--orange)"/><rect x="22" y="6" width="16" height="10" fill="none" stroke="var(--orange)" stroke-width="3"/></svg>Office Productivity<br>&amp; Collaboration</div>
  <div class="biz-item" style="left:709px;top:255px"><svg width="60" height="50" viewBox="0 0 60 50"><rect x="8" y="6" width="44" height="30" rx="2" fill="none" stroke="var(--orange)" stroke-width="3"/><path d="M22 46h16M30 36v10" stroke="var(--orange)" stroke-width="3"/></svg>Virtual Desktops</div>
  <div class="biz-item" style="left:922px;top:255px"><svg width="60" height="50" viewBox="0 0 60 50"><circle cx="30" cy="26" r="20" fill="none" stroke="var(--orange)" stroke-width="4"/><text x="30" y="32" text-anchor="middle" font-size="15" font-weight="700" fill="var(--orange)" font-family="Arial,sans-serif">24</text></svg>Help Desk</div>

  <div class="biz-item" style="left:72px;top:465px"><svg width="60" height="50" viewBox="0 0 60 50"><rect x="8" y="6" width="44" height="34" fill="none" stroke="var(--orange)" stroke-width="3"/><path d="M34 20l12 4c0 10-6 16-12 20-6-4-12-10-12-20z" fill="var(--orange)"/></svg>Anti-Virus /<br>Anti-Spam and<br>Web Filtering</div>
  <div class="biz-item" style="left:278px;top:465px"><svg width="60" height="50" viewBox="0 0 60 50"><rect x="12" y="4" width="36" height="26" rx="3" fill="var(--orange)"/><rect x="6" y="34" width="48" height="12" fill="var(--orange)"/></svg>Business<br>Communications</div>
  <div class="biz-item" style="left:492px;top:465px"><svg width="60" height="50" viewBox="0 0 60 50"><circle cx="30" cy="18" r="6" fill="var(--orange)"/><path d="M18 8a16 16 0 0 0 0 20M42 8a16 16 0 0 1 0 20M30 24l-10 24h20z" stroke="var(--orange)" stroke-width="3" fill="none"/></svg>Open Source<br>Technologies</div>
  <div class="biz-item" style="left:709px;top:465px"><svg width="60" height="50" viewBox="0 0 60 50"><rect x="10" y="6" width="18" height="18" fill="var(--orange)"/><rect x="32" y="6" width="18" height="18" fill="var(--orange)"/><rect x="10" y="28" width="18" height="18" fill="var(--orange)"/><rect x="32" y="28" width="18" height="18" fill="var(--orange)"/></svg>Custom IT<br>Solutions</div>

  <div class="divider" style="top:610px"></div>

  <div class="sub-title" style="top:700px">IT SERVICES</div>
  <div class="sub-note" style="top:746px">Tailored for your IT challenges</div>

  <div class="tab active" style="left:78px;top:815px"><svg width="48" height="48" viewBox="0 0 48 48"><circle cx="24" cy="24" r="20" fill="none" stroke="#fff" stroke-width="6"/><circle cx="24" cy="24" r="8" fill="none" stroke="#fff" stroke-width="4"/></svg>Remote Help<br>Desk Support</div>
  <div class="tab" style="left:252px;top:815px"><svg width="48" height="48" viewBox="0 0 48 48"><circle cx="18" cy="28" r="12" fill="none" stroke="#444" stroke-width="5" stroke-dasharray="5 3"/><circle cx="36" cy="12" r="7" fill="none" stroke="#444" stroke-width="4" stroke-dasharray="4 2"/></svg>Hardware<br>Management<br>and Support</div>
  <div class="tab" style="left:426px;top:815px"><svg width="48" height="48" viewBox="0 0 48 48"><path d="M6 20a26 26 0 0 1 36 0M12 27a17 17 0 0 1 24 0M18 34a8 8 0 0 1 12 0" fill="none" stroke="#444" stroke-width="4"/><circle cx="24" cy="41" r="3" fill="#444"/></svg>Network Security<br>&amp; Management</div>
  <div class="tab" style="left:600px;top:815px"><svg width="48" height="48" viewBox="0 0 48 48"><ellipse cx="22" cy="10" rx="16" ry="6" fill="#444"/><path d="M6 10v26c0 3 7 6 16 6s16-3 16-6V10" fill="#444"/><circle cx="38" cy="36" r="8" fill="#dcdcdc" stroke="#444" stroke-width="3"/></svg>Data Backup &amp;<br>Recovery</div>
  <div class="tab" style="left:774px;top:815px"><svg width="48" height="48" viewBox="0 0 48 48"><rect x="4" y="6" width="40" height="28" fill="none" stroke="#444" stroke-width="3"/><path d="M10 28l8-10 8 6 12-12" fill="none" stroke="#444" stroke-width="3"/><path d="M16 42h16" stroke="#444" stroke-width="3"/></svg>Performance &amp;<br>Availability<br>Monitoring</div>
  <div class="tab" style="left:948px;top:815px"><svg width="48" height="48" viewBox="0 0 48 48"><path d="M24 4l18 6c0 18-8 28-18 34C14 38 6 28 6 10z" fill="#444"/></svg>Managed<br>Security &amp;<br>Compliance</div>

  <div class="tab-detail">
    <h3>Remote Help <b>Desk<br>Support</b></h3>
    <div class="btn-orange" style="left:78px;top:1127px">CONTACT US</div>
    <p style="top:1033px">Lorem Ipsum is simply dummy text of the printing and typesetting industry. Lorem Ipsum has been the industry's standard dummy text ever since the 1500s, when an unknown printer took a galley of type and scrambled it to make a type specimen book.</p>
    <p style="top:1130px">Lorem Ipsum is simply dummy text of the printing and typesetting industry. Lorem Ipsum has been the industry's standard dummy text ever since the 1500.</p>
  </div>

  <div class="tab" style="left:78px;top:1228px"><svg width="48" height="48" viewBox="0 0 48 48"><rect x="8" y="8" width="32" height="22" fill="none" stroke="#444" stroke-width="3"/><path d="M2 36h44" stroke="#444" stroke-width="4"/></svg>Hardware &amp;<br>Software Asset<br>Management</div>
  <div class="tab" style="left:252px;top:1228px"><svg width="48" height="48" viewBox="0 0 48 48"><rect x="8" y="26" width="8" height="16" fill="#444"/><rect x="20" y="18" width="8" height="24" fill="#444"/><rect x="32" y="8" width="8" height="34" fill="#444"/></svg>Capacity<br>Planning &amp;<br>Forecasting</div>
  <div class="tab" style="left:426px;top:1228px"><svg width="48" height="48" viewBox="0 0 48 48"><path d="M10 4h20l8 8v32H10z" fill="none" stroke="#444" stroke-width="3"/><path d="M16 22h16M16 30h16M16 38h10" stroke="#444" stroke-width="3"/></svg>Business Impact<br>Analysis</div>
  <div class="tab" style="left:600px;top:1228px"><svg width="48" height="48" viewBox="0 0 48 48"><circle cx="24" cy="10" r="6" fill="#444"/><rect x="18" y="18" width="12" height="16" fill="#444"/><circle cx="8" cy="20" r="4" fill="#444"/><circle cx="40" cy="20" r="4" fill="#444"/><rect x="4" y="26" width="8" height="14" fill="#444"/><rect x="36" y="26" width="8" height="14" fill="#444"/></svg>Vendor<br>Management</div>
  <div class="tab" style="left:774px;top:1228px"><svg width="48" height="48" viewBox="0 0 48 48"><circle cx="24" cy="24" r="18" fill="none" stroke="#444" stroke-width="4"/><circle cx="24" cy="24" r="10" fill="none" stroke="#444" stroke-width="4"/><circle cx="24" cy="24" r="3" fill="#444"/></svg>Virtual CIO</div>

  <div class="sub-title" style="top:1528px;line-height:44px">SOFTWARE IMPLEMENTATION &amp;<br>CONSULTING</div>

  <div class="card" style="left:78px"><svg width="60" height="50" viewBox="0 0 60 50"><path d="M15 40h32a10 10 0 0 0 0-20 14 14 0 0 0-27-3 11 11 0 0 0-5 23z" fill="var(--orange)"/></svg>Cloud Services<span class="more">LEARN MORE</span></div>
  <div class="card" style="left:292px"><svg width="60" height="50" viewBox="0 0 60 50"><circle cx="30" cy="22" r="16" fill="var(--orange)"/><circle cx="30" cy="22" r="6" fill="#fff"/><rect x="18" y="40" width="24" height="6" fill="var(--orange)"/></svg>Open Source<br>Software<span class="more">LEARN MORE</span></div>
  <div class="card" style="left:505px"><svg width="60" height="50" viewBox="0 0 60 50"><rect x="16" y="4" width="28" height="42" rx="3" fill="var(--orange)"/><rect x="21" y="9" width="18" height="10" fill="#fff"/></svg>Enterprise<br>Resource Planning<span class="more">LEARN MORE</span></div>
  <div class="card" style="left:718px"><svg width="60" height="50" viewBox="0 0 60 50"><circle cx="30" cy="12" r="8" fill="var(--orange)"/><path d="M16 46a14 14 0 0 1 28 0z" fill="var(--orange)"/></svg>Customer<br>Relationship<br>Management<span class="more">LEARN MORE</span></div>
  <div class="card" style="left:932px"><svg width="60" height="50" viewBox="0 0 60 50"><rect x="10" y="28" width="40" height="6" fill="var(--orange)"/><rect x="28" y="8" width="18" height="16" fill="var(--orange)"/><circle cx="18" cy="14" r="6" fill="var(--orange)"/><rect x="14" y="34" width="4" height="12" fill="var(--orange)"/><rect x="42" y="34" width="4" height="12" fill="var(--orange)"/></svg>Professional<br>Services<span class="more">LEARN MORE</span></div>
</section>

<section class="about">
  <h2 class="section-title" style="top:62px">ABOUT <span>US</span></h2>
  <p>Based in the beautiful Sorrel Valley and surrounded by the Meridel Ridge, Meridel Falls Technology Group is a best-in-class technology partner providing a wide range of business solutions, IT services, cloud services, software implementation and consulting. Our services are professional, accessible, and results-oriented, but what makes us stand out from our competitors is the individual attention we give to each of our clients. Let us help you with your existing IT needs or help you find the latest technology solutions to move your business forward and leave IT headaches behind. Get in touch with our team of industry experts for an initial assessment.</p>
  <div class="value" style="left:72px"><div class="dot"><svg width="56" height="40" viewBox="0 0 56 40"><path d="M4 20l12-12 12 8 12-8 12 12-16 14-8-6-8 6z" fill="#fff"/></svg></div>Trusted<br>Technology<br>Partner</div>
  <div class="value" style="left:285px"><div class="dot"><svg width="50" height="50" viewBox="0 0 50 50"><circle cx="25" cy="16" r="10" fill="#fff"/><path d="M8 46a17 17 0 0 1 34 0z" fill="#fff"/></svg></div>Customer<br>First</div>
  <div class="value" style="left:495px"><div class="dot"><svg width="50" height="50" viewBox="0 0 50 50"><circle cx="25" cy="20" r="12" fill="none" stroke="#fff" stroke-width="4"/><rect x="19" y="34" width="12" height="8" fill="#fff"/></svg></div>Industry<br>Experts</div>
  <div class="value" style="left:709px"><div class="dot"><svg width="56" height="44" viewBox="0 0 56 44"><circle cx="28" cy="12" r="8" fill="#fff"/><circle cx="12" cy="18" r="6" fill="#fff"/><circle cx="44" cy="18" r="6" fill="#fff"/><path d="M16 42a12 12 0 0 1 24 0zM2 42a10 10 0 0 1 16-8M54 42a10 10 0 0 0-16-8" fill="#fff"/></svg></div>Professional<br>Staff</div>
  <div class="value" style="left:926px"><div class="dot"><svg width="50" height="50" viewBox="0 0 50 50"><circle cx="20" cy="28" r="12" fill="none" stroke="#fff" stroke-width="6" stroke-dasharray="5 3"/><circle cx="36" cy="12" r="7" fill="none" stroke="#fff" stroke-width="4" stroke-dasharray="4 2"/></svg></div>Latest<br>Technologies</div>
</section>

<section class="team">
  <h2 class="section-title" style="top:58px">OUR <span>TEAM</span></h2>
  <div class="member" style="left:80px"><div class="avatar" role="img" aria-label="Team member portrait placeholder"></div>Systems Engineer</div>
  <div class="member" style="left:343px"><div class="avatar" role="img" aria-label="Team member portrait placeholder"></div>DevOps Engineer</div>
  <div class="member" style="left:614px"><div class="avatar" role="img" aria-label="Team member portrait placeholder"></div>Software Engineer</div>
  <div class="member" style="left:886px"><div class="avatar" role="img" aria-label="Team member portrait placeholder"></div>Sales Engineer</div>
</section>

<section class="partners">
  <h2 class="section-title" style="top:50px">OUR <span>PARTNERS</span></h2>
  <div class="partner-row" style="left:50px;top:128px;width:1040px">
    <div class="partner">Corvane</div>
    <div class="partner">Lindgate</div>
    <div class="partner">Virtalon</div>
    <div class="partner">Orvessa</div>
    <div class="partner">Cloudmere</div>
    <div class="partner">Tidewire</div>
  </div>
  <div class="partner-row" style="left:220px;top:218px;width:760px">
    <div class="partner small">Brightvale<br>Web Services</div>
    <div class="partner small">Lindgate<br>Skyline</div>
    <div class="partner">Quorlith</div>
  </div>
</section>

<footer class="footer">
  <h4 style="left:78px;top:50px">GET IN TOUCH WITH US</h4>
  <div class="rule" style="left:78px;top:112px;width:460px"></div>
  <div class="field" style="left:78px;top:150px;width:255px">Enter Name</div>
  <div class="field" style="left:353px;top:150px;width:255px">Enter Contact No.</div>
  <div class="field" style="left:78px;top:212px;width:530px">Enter Email Id</div>
  <div class="field" style="left:78px;top:272px;width:530px;height:100px">Enter Message</div>
  <div class="submit">SUBMIT</div>

  <h4 style="left:728px;top:50px">CONTACT INFO</h4>
  <div class="rule" style="left:728px;top:112px;width:388px"></div>
  <div class="info" style="top:150px"><svg width="14" height="20" viewBox="0 0 14 20"><path d="M7 0a7 7 0 0 1 7 7c0 5-7 13-7 13S0 12 0 7a7 7 0 0 1 7-7z" fill="#fff"/><circle cx="7" cy="7" r="2.5" fill="#4a4a4a"/></svg><span>Lorem Ipsum is simply<br>dummy text of the printing.</span></div>
  <div class="info" style="top:210px"><svg width="16" height="18" viewBox="0 0 16 18"><path d="M3 0l4 4-2 3c1 2 3 4 5 5l3-2 3 4-3 3C7 17-1 9 0 3z" fill="#fff"/></svg><span>123 456 7890</span></div>
  <div class="info" style="top:245px"><svg width="18" height="14" viewBox="0 0 18 14"><rect width="18" height="14" fill="#fff"/><path d="M0 0l9 7 9-7" fill="none" stroke="#4a4a4a" stroke-width="1.5"/></svg><span>info@meridelfallstech.com</span></div>
  <div class="follow">FOLLOW US</div>
  <div class="social-foot" aria-label="Social links"><span></span><span></span><span></span></div>

  <div class="bottom-line"></div>
  <ul class="foot-links"><li>Home</li><li>About Us</li><li>Services</li><li>Our team</li><li>Partner</li><li>Contact Us</li></ul>
  <div class="copy">© <b>Meridel Falls technology group</b> - 2016. All Rights Reserved.</div>
</footer>

</body>
</html>
```